Copperfield Capital Partners Web Design

Copperfield Capital Partners is a national strategic business consulting company serving both marijuana businesses and investors. We assist emerging businesses in the marijuana sector that need assistance in developing their brand awareness and investor visibility within the industry. In addition, we provide information about these companies to investors so the can make financial decisions and discuss them in our forums. We would like to see designs that use the colors green, black and grey but please feel free to use your imagination. The final design should communicate financial growth

Target Market(s)

21-55+ men willing to invest in the marijuana market. These are savvy people who are expect to see a professional website.

Industry/Entity Type

Business

Coding

Coded - Design and coding required

Number of Pages Required

5+ page

Font styles to use
Serif
Sans Serif

Colors
abd036
cadf82
9bcb3c
c3c3c3
ffffff
000000

Requirements
Must have
• A Homepage, About Us page, Contact Us page, Watch List, Forums, a Disclaimer page, Privacy Policy and a "Watch List" page for us to promote marijuana companies on. We need a section to ask for visitor email addresses to join our mailing list. The site must be simple to navigate, but professional. If you were going to invest money into a risky marijuana market, what kind of website would you trust to get your information from?
Nice to have
• Our Facebook and Twitter integrated:
• www.facebook.com/CopperfieldCapitalPartners
• twitter.com/CopperfieldCP
• It would be nice if we could have a rolling comments section, where visitors can use facebook or whatever to post a quick comment. Maybe a testimonials page.
• It would be nice to have a blog page.

```html
<!DOCTYPE html>
<html lang="en">
<head>
<meta charset="utf-8">
<title>Copperfield Capital Partners</title>
<link rel="stylesheet" href="https://fonts.googleapis.com/css2?family=Cinzel:wght@400;700&family=Open+Sans:wght@400;700&family=Arimo:wght@400;700&display=swap">
<style>
:root{
  --green:#6aa524;
  --green-dark:#4f8a1c;
  --lime:#9bcb3c;
  --lime-light:#abd036;
  --pale:#cadf82;
  --grey:#c3c3c3;
  --ink:#2b3547;
  --panel:#3a3a3a;
  --dark:#1d1d1d;
  --black:#000;
  --white:#fff;
}
*{margin:0;padding:0;box-sizing:border-box}
html,body{width:726px;height:1200px;overflow:hidden}
body{position:relative;background:var(--dark);font-family:Arimo,Arial,sans-serif;color:var(--white)}
.abs{position:absolute}
.serif{font-family:Cinzel,Georgia,serif}

.site-header{left:0;top:0;width:726px;height:65px;background:var(--white)}
.brand{left:132px;top:14px;display:flex;align-items:center;gap:8px}
.brand-mark{width:20px;height:20px;background:var(--green)}
.brand-name{font-family:Cinzel,Georgia,serif;font-size:13px;color:var(--green);letter-spacing:.5px;white-space:nowrap}
.social{display:flex;gap:6px}
.social span{width:11px;height:11px;border-radius:50%;background:#2a2a2a;display:block}
.header-social{left:532px;top:21px}

.nav-ribbon{left:104px;top:50px;width:518px;height:28px}
.main-nav{left:132px;top:48px;width:462px;height:27px;background:var(--green);display:flex;justify-content:space-around;align-items:center;box-shadow:0 2px 3px rgba(0,0,0,.3)}
.main-nav a{font-family:Cinzel,Georgia,serif;color:var(--white);text-decoration:none;font-size:9.5px;letter-spacing:.3px}

.hero{left:0;top:65px;width:726px;height:256px;background:radial-gradient(ellipse at 60% 50%,#3e5a24 0%,#26391a 60%,#1a2812 100%)}
.hero-portrait{left:130px;top:17px;width:190px;height:239px;background:linear-gradient(180deg,#8a8a86 0%,#4d4d4b 45%,#3a3a3a 100%);border-radius:70px 70px 0 0}
.hero-text{left:342px;top:67px;width:260px;font-size:13.6px;line-height:15px;color:var(--white);letter-spacing:.1px}
.hero-text em{font-style:normal;color:var(--lime-light)}
.btn{background:var(--lime-light);color:var(--white);font-family:Cinzel,Georgia,serif;font-weight:700;font-size:8.5px;display:flex;align-items:center;justify-content:center}
.hero-btn{left:342px;top:153px;width:82px;height:22px}

.why-panel{left:103px;top:321px;width:519px;height:135px;background:var(--panel)}
.why-art{left:44px;top:46px;width:140px;height:64px;background:linear-gradient(160deg,#4fa3e0 0%,#2d6fb0 50%,#1a1a1a 100%);border-radius:6px;transform:skewX(-12deg)}
.why-title{left:151px;top:30px;font-size:16.5px;color:var(--white);white-space:nowrap}
.why-copy{left:206px;top:60px;width:272px;font-size:7.3px;line-height:8.6px;color:#cfcfcf}

.blogs-panel{left:103px;top:456px;width:519px;height:387px;background:var(--white);color:var(--ink)}
.blogs-title{left:0;top:21px;width:519px;text-align:center;font-size:17px;color:var(--ink)}
.blogs-sub{left:0;top:44px;width:519px;text-align:center;font-size:7.2px;color:#666}
.thumb{border:1px solid #d8d8d8}
.post-title{font-family:'Open Sans',Arial,sans-serif;font-weight:700;color:#2b3547}
.post-copy{font-size:7.1px;line-height:8.4px;color:#3d4b6a}
.lg-title{font-size:10.2px;white-space:nowrap}
.sm-title{font-size:7.2px;line-height:8.8px;width:115px;max-height:17.6px;overflow:hidden;display:-webkit-box;-webkit-line-clamp:2;-webkit-box-orient:vertical}

.testimonials{left:0;top:830px;width:726px;height:175px;background:var(--panel)}
.test-title{left:0;top:33px;width:726px;text-align:center;font-size:17px;color:var(--white)}
.quote-mark{left:174px;top:50px;font-family:Georgia,serif;font-size:60px;color:#7a7a7a;line-height:1}
.quote-text{left:224px;top:61px;width:292px;font-size:7.2px;line-height:8.7px;color:#cfcfcf}
.quote-by{left:224px;top:114px;font-size:9.2px;font-weight:700;color:var(--lime)}
.dots{left:225px;top:137px;display:flex;gap:4px}
.dots span{width:7px;height:7px;border-radius:50%;background:#d0d0d0}
.dots span.on{background:var(--lime)}

.newsletter{left:0;top:1005px;width:726px;height:103px;background:var(--black)}
.news-title{left:0;top:21px;width:726px;text-align:center;font-size:13px;color:var(--white)}
.news-sub{left:0;top:39px;width:726px;text-align:center;font-size:7.3px;color:#6a6a6a}
.news-input{left:286px;top:57px;width:121px;height:16px;background:var(--white);color:#333;font-size:7px;padding:4px 6px}
.news-btn{left:407px;top:57px;width:40px;height:16px;background:var(--lime);color:var(--white);font-size:7px;display:flex;align-items:center;justify-content:center}

.site-footer{left:0;top:1108px;width:726px;height:92px;background:#1a1a1a}
.footer-brand{left:106px;top:30px;display:flex;align-items:center;gap:8px}
.footer-brand .brand-mark{background:var(--white)}
.footer-brand .brand-name{color:var(--white);font-size:12px}
.footer-social{left:554px;top:24px}
.footer-social span{background:#9a9a9a;width:12px;height:12px}
.footer-nav{right:103px;top:46px;display:flex;gap:12px}
.footer-nav a{font-family:Cinzel,Georgia,serif;font-size:6.6px;color:#d8d8d8;text-decoration:none;white-space:nowrap}
.copyright{right:103px;top:59px;font-size:6px;color:#bdbdbd}
</style>
</head>
<body>

<header class="site-header abs">
  <div class="brand abs"><span class="brand-mark"></span><span class="brand-name">Copperfield Capital Partners</span></div>
  <div class="social header-social abs" aria-label="Social links"><span></span><span></span><span></span><span></span></div>
</header>

<svg class="nav-ribbon abs" viewBox="0 0 518 28" aria-hidden="true">
  <polygon points="0,0 28,0 28,26 20,22" fill="#4f8a1c"/>
  <polygon points="518,0 490,0 490,26 498,22" fill="#4f8a1c"/>
</svg>
<nav class="main-nav abs">
  <a href="#">Home</a><a href="#">About Us</a><a href="#">Watch List</a><a href="#">Testimonials</a><a href="#">Blog</a><a href="#">Contact Us</a>
</nav>

<section class="hero abs" role="img" aria-label="Background of green cannabis leaves">
  <div class="hero-portrait abs" role="img" aria-label="Photo of a smiling advisor in a grey suit"></div>
  <p class="hero-text abs serif">We assist <em>emerging businesses</em> in the marijuana sector that need assistance in <em>developing their brand awareness</em> and investor visibility within the industry.</p>
  <a class="hero-btn btn abs">KNOW MORE</a>
</section>

<section class="why-panel abs">
  <div class="why-art abs" role="img" aria-label="Illustration of a tablet with a rising bar chart"></div>
  <h2 class="why-title abs serif" style="font-weight:400">Why invest in marijuana business?</h2>
  <p class="why-copy abs">Lorem ipsum dolor sit amet, consectetur adipiscing elit, sed do eiusmod tempor incididunt ut labore et dolore magna aliqua. Ut enim ad minim veniam, quis nostrud exercitation ullamco laboris nisi ut aliquip ex ea commodo consequat. Duis aute irure dolor in in voluptate velit esse cillum dolore eu fugiat nulla pariatur.</p>
</section>

<section class="blogs-panel abs">
  <h2 class="blogs-title abs serif" style="font-weight:400">Latest Blogs</h2>
  <p class="blogs-sub abs">Lorem ipsum dolor sit amet, consectetur adipiscing elit, sed do tempor incididunt ut et dolore magna aliqua.</p>

  <div class="thumb abs" style="left:12px;top:69px;width:239px;height:102px;background:linear-gradient(90deg,#6b7d3a,#8a9a4a 55%,#b46a4a)" role="img" aria-label="Photo of a worker inspecting cannabis plants in a grow facility"></div>
  <h3 class="post-title lg-title abs" style="left:12px;top:181px">Medical marijuana production in Canada set ...</h3>
  <p class="post-copy abs" style="left:12px;top:198px;width:240px">VANCOUVER — Martin Hale doesn't fit the stereotypical image of a marijuana grower. Neither do his two partners at Harborline Ventures Inc., a Seattle-based venture capital firm.</p>

  <div class="thumb abs" style="left:268px;top:69px;width:239px;height:102px;background:linear-gradient(90deg,#8a2a1a,#3a5a2a 35%,#2a2a2a 55%,#a89a2a)" role="img" aria-label="Illustration of a pipe-smoking figure before a striped flag"></div>
  <h3 class="post-title lg-title abs" style="left:268px;top:181px">Marijuana's Long Term Effects Revealed</h3>
  <p class="post-copy abs" style="left:268px;top:198px;width:240px">Marijuana has many documented physical benefits on the user and thousands of industrial uses that could eliminate the wanton pillaging of our natural resources. Yet, it's made illegal for personal use.</p>

  <div class="thumb abs" style="left:12px;top:239px;width:113px;height:48px;background:linear-gradient(90deg,#8a8a5a,#b0a86a)" role="img" aria-label="Photo of dried cannabis buds"></div>
  <h4 class="post-title sm-title abs" style="left:12px;top:297px">Marijuana Commodity Exchanges Hover the Horizon</h4>
  <p class="post-copy abs" style="left:12px;top:319px;width:112px">Marijuana federal laws will have to change dramatically before a marijuana commodity exchange can become fully operational, but there are already.</p>

  <div class="thumb abs" style="left:136px;top:239px;width:113px;height:48px;background:linear-gradient(90deg,#e4e0d4,#9a9a6a)" role="img" aria-label="Photo of capsules and cannabis buds"></div>
  <h4 class="post-title sm-title abs" style="left:136px;top:297px">Medical marijuana seeds</h4>
  <p class="post-copy abs" style="left:136px;top:310px;width:112px">Medical marijuana is becoming more popular these days. Finally laws are adapted for the purpose of "medical marijuana use" worldwide.</p>

  <div class="thumb abs" style="left:261px;top:239px;width:113px;height:48px;background:linear-gradient(180deg,#c8ccc0,#3d6a2a)" role="img" aria-label="Photo of a hand holding a seedling in a greenhouse"></div>
  <h4 class="post-title sm-title abs" style="left:261px;top:297px">Health Board clamps down on medical marijuana advertising</h4>
  <p class="post-copy abs" style="left:261px;top:319px;width:112px">National Health Board has ordered the medical marijuana companies to stop making their products look so good.</p>

  <div class="thumb abs" style="left:385px;top:239px;width:113px;height:48px;background:linear-gradient(90deg,#6a5a3a,#d8d4c8)" role="img" aria-label="Photo of cannabis in a paper bag"></div>
  <h4 class="post-title sm-title abs" style="left:385px;top:297px">Wichita to vote on reduced marijuana penalties</h4>
  <p class="post-copy abs" style="left:385px;top:319px;width:112px">The Wichita city council has voted to put an issue on the April election ballot to allow for reduced penalties for first-time marijuana possession, but the long-term prospects.</p>
</section>

<section class="testimonials abs">
  <h2 class="test-title abs serif" style="font-weight:700">Testimonials</h2>
  <div class="quote-mark abs" aria-hidden="true">&ldquo;</div>
  <p class="quote-text abs">Sed ut perspiciatis, unde omnis iste natus error sit voluptatem accusantium doloremque laudantium, totam rem aperiam eaque ipsa, quae ab illo inventore veritatis et quasi architecto beatae vitae dicta sunt, explicabo. Nemo enim ipsam voluptatem, quia voluptas sit, aspernatur aut odit aut fugit, sed quia consequuntur magni dolores eos, qui ratione voluptatem sequi nesciunt, neque porro quisquam est, qui dolorem ipsum,.</p>
  <p class="quote-by abs">Director, Ridgeway Capital</p>
  <div class="dots abs"><span class="on"></span><span></span><span></span><span></span></div>
</section>

<section class="newsletter abs">
  <h2 class="news-title abs serif" style="font-weight:400">Subscribe to Newsletter</h2>
  <p class="news-sub abs">Lorem ipsum dolor sit amet, consectetur adipisicing elit, sed do eiusmod tempor</p>
  <div class="news-input abs">enter email</div>
  <div class="news-btn abs">submit</div>
</section>

<footer class="site-footer abs">
  <div class="footer-brand abs"><span class="brand-mark"></span><span class="brand-name">Copperfield Capital Partners</span></div>
  <div class="social footer-social abs" aria-label="Social links"><span></span><span></span><span></span><span></span></div>
  <nav class="footer-nav abs">
    <a href="#">Home</a><a href="#">About Us</a><a href="#">Watch List</a><a href="#">Testimonials</a><a href="#">Blog</a><a href="#">Contact Us</a>
  </nav>
  <p class="copyright abs">Copyright © 2015. All rights reserved</p>
</footer>

</body>
</html>
```